Need Power Point Presentation - That incorporates New Logo

We have a new logo and would like to incorporate it into a Power Point template. We are looking for title page, 2 body pages and a closing page design. If you have any questions please let me know. New logo is attached.

```html
<!DOCTYPE html>
<html lang="en">
<head>
<meta charset="utf-8">
<title>Presentation Body Slide</title>
<link rel="stylesheet" href="https://fonts.googleapis.com/css2?family=Arimo:wght@400&display=swap">
<style>
  :root {
    --page-bg: #ffffff;
    --slide-light: #f1f1f1;
    --slide-mid: #dedede;
    --panel-bottom: #e2e2e2;
    --curve-line: #a9a9a9;
    --body-text: #111111;
    --brand-text: #555555;
  }
  * { margin: 0; padding: 0; box-sizing: border-box; }
  html, body {
    width: 1200px;
    height: 1000px;
    overflow: hidden;
    background: var(--page-bg);
  }
  .slide {
    position: absolute;
    left: 128px;
    top: 125px;
    width: 960px;
    height: 718px;
    overflow: hidden;
    background: linear-gradient(135deg, var(--slide-light) 0%, var(--slide-mid) 100%);
    box-shadow: 8px 10px 22px rgba(0, 0, 0, 0.45);
  }
  .slide-curves {
    position: absolute;
    inset: 0;
    width: 960px;
    height: 718px;
  }
  .body-copy {
    position: absolute;
    left: 66px;
    top: 131px;
    width: 680px;
    white-space: nowrap;
    font-family: "Arimo", Arial, sans-serif;
    font-size: 22px;
    letter-spacing: 0.8px;
    line-height: 28.8px;
    color: var(--body-text);
  }
  .brand-name {
    position: absolute;
    left: 792px;
    top: 655px;
    font-family: "Arimo", Arial, sans-serif;
    font-size: 22px;
    color: var(--brand-text);
  }
</style>
</head>
<body>
  <section class="slide">
    <svg class="slide-curves" viewBox="0 0 960 718" aria-hidden="true">
      <defs>
        <linearGradient id="panel-fill" x1="0" y1="0" x2="1" y2="1">
          <stop offset="0" stop-color="#d4d4d4"/>
          <stop offset="1" stop-color="#c2c2c2"/>
        </linearGradient>
      </defs>
      <path d="M640,0 C760,110 832,270 826,410 C820,540 760,650 672,718 L960,718 L960,0 Z" fill="url(#panel-fill)"/>
      <path d="M0,675 C330,695 700,620 960,497 L960,718 L0,718 Z" fill="var(--panel-bottom)" opacity="0.85"/>
      <path d="M640,0 C760,110 832,270 826,410 C820,540 760,650 672,718" fill="none" stroke="var(--curve-line)" stroke-width="2.5"/>
      <path d="M0,675 C330,695 700,620 960,497" fill="none" stroke="var(--curve-line)" stroke-width="2.5"/>
    </svg>

    <p class="body-copy">
      Lorem ipsum dolor sit amet, consectetuer adipiscing elit,<br>
      sed diam nonummy nibh euismod tincidunt ut laoreet<br>
      dolore magna aliquam erat volutpat. Ut wisi enim ad<br>
      minim veniam, quis nostrud exerci tation ullamcorper<br>
      suscipit lobortis nisl ut aliquip ex ea commodo<br>
      consequat. Duis autem vel eum iriure dolor in hendrerit<br>
      in vulputate velit esse molestie consequat, vel illum<br>
      dolore eu feugiat nulla facilisis at vero eros et accumsan<br>
      et iusto odio dignissim qui blandit praesent luptatum zzril<br>
      delenit augue duis dolore te feugait nulla facilisi. Nam<br>
      liber tempor cum soluta nobis eleifend option congue<br>
      nihil imperdiet doming id quod mazim placerat facer<br>
      possim assum. Typi non habent claritatem insitam; est<br>
      usus legentis in iis qui facit eorum claritatem.<br>
      Investigationes demonstraverunt lectores legere me lius<br>
      quod ii legunt saepius.
    </p>

    <span class="brand-name">Norvane</span>
  </section>
</body>
</html>
```